Business Card Design For A Renovation Contractor Company

We need a business card for a new company based in Singapore, our company name is "KT Planora". We are a renovation contractor that builds designs into reality. We build more of F&B restaurants, retail stores and commercial offices. We work very closely with designers. The final design should communicate to our client that we are a company that you can trust, that will plan and complete your project without giving you a headache. I like my client to remember my company as "KT". The beauty of SIMPLE is important.

Industry/Entity Type

Contractor

Requirements
Nice to have
• Black or Red base

```html
<!DOCTYPE html>
<html lang="en">
<head>
<meta charset="utf-8">
<title>KT Planora — Business Card</title>
<link rel="stylesheet" href="https://fonts.googleapis.com/css2?family=Open+Sans:wght@400;600&family=Tinos:wght@700&display=swap">
<style>
  :root {
    --backdrop: #e9e6e2;
    --card-white: #f7f7f7;
    --card-black: #232323;
    --card-black-edge: #2d2d2d;
    --accent-red: #d8232a;
    --ink-dark: #2b2b2b;
    --ink-light: #f2f2f2;
    --ink-muted: #bdbdbd;
  }
  * { box-sizing: border-box; margin: 0; padding: 0; }
  html, body { width: 1200px; height: 723px; overflow: hidden; }
  body {
    background: var(--backdrop);
    font-family: "Open Sans", Arial, sans-serif;
    display: flex;
    align-items: center;
    justify-content: center;
    gap: 80px;
  }
  .card {
    width: 340px;
    height: 595px;
    border-radius: 3px;
    box-shadow: 0 10px 28px rgba(0,0,0,0.18);
    position: relative;
  }
  /* Front */
  .card-front {
    background: var(--card-white);
    display: flex;
    flex-direction: column;
    align-items: center;
    justify-content: center;
    gap: 22px;
  }
  .brand-dot {
    width: 150px;
    height: 150px;
    border-radius: 50%;
    background: var(--accent-red);
  }
  .front-name {
    font-size: 34px;
    font-weight: 600;
    color: var(--ink-dark);
    letter-spacing: 0.5px;
  }
  /* Back */
  .card-back {
    background: radial-gradient(ellipse at 40% 35%, var(--card-black-edge), var(--card-black) 70%);
    color: var(--ink-light);
    padding: 44px 30px 0 40px;
  }
  .brand-lockup {
    display: flex;
    flex-direction: column;
    align-items: flex-end;
  }
  .brand-row {
    display: flex;
    align-items: center;
    gap: 12px;
  }
  .brand-mark {
    width: 34px;
    height: 34px;
    border-radius: 50%;
    background: var(--accent-red);
  }
  .brand-name {
    font-size: 36px;
    font-weight: 600;
    color: var(--ink-light);
    line-height: 1.1;
  }
  .brand-rule {
    width: 100%;
    height: 1px;
    background: var(--ink-muted);
    margin-top: 6px;
  }
  .brand-tagline {
    font-size: 14px;
    color: var(--ink-light);
    margin-top: 3px;
    letter-spacing: 0.3px;
  }
  .person {
    margin-top: 58px;
  }
  .person-name {
    font-family: "Tinos", "Times New Roman", serif;
    font-weight: 700;
    font-size: 19px;
    letter-spacing: 0.5px;
    text-transform: uppercase;
  }
  .person-title {
    color: var(--accent-red);
    font-size: 15px;
    font-weight: 600;
    margin-top: 2px;
  }
  .address {
    margin-top: 18px;
    font-size: 14px;
    line-height: 1.5;
  }
  .contacts {
    list-style: none;
    margin-top: 28px;
    font-size: 15px;
    line-height: 1.6;
  }
  .contacts .label {
    color: var(--accent-red);
    font-weight: 600;
    display: inline-block;
    width: 24px;
  }
</style>
</head>
<body>
  <section class="card card-front" aria-label="Card front">
    <div class="brand-dot"></div>
    <p class="front-name">KT Planora</p>
  </section>

  <section class="card card-back" aria-label="Card back">
    <div class="brand-lockup">
      <div class="brand-row">
        <span class="brand-mark"></span>
        <span class="brand-name">KT Planora</span>
      </div>
      <div class="brand-rule"></div>
      <p class="brand-tagline">turning plans into spaces</p>
    </div>

    <div class="person">
      <p class="person-name">Daniel Koh</p>
      <p class="person-title">President</p>
      <p class="address">27 Tanjong Pagar Road, #03-12<br>Singapore 088451</p>
    </div>

    <ul class="contacts">
      <li><span class="label">T:</span> +65 6123 4567</li>
      <li><span class="label">F:</span> +65 6123 4568</li>
      <li><span class="label">E:</span> hello@ktplanora.sg</li>
      <li><span class="label">W:</span> www.ktplanora.sg</li>
    </ul>
  </section>
</body>
</html>
```